FULLY CUSTOM MAIN BANNER IMAGE FOR MY WEBSITE-REDESIGN CURRENT

SIZE MUST BE: 1800x829

LOOKING FOR A FULLY CUSTOM MAIN BANNER IMAGE TO BE DESIGNED FOR MY NEW WEBSITE HOMEPAGE http://gridplankstudio.com/dh/derek/vtr_final/index.html THE CONTENT THAT YOU SEE ON THE UPLOADED FILE OR HERE http://gridplankstudio.com/dh/derek/vtr_final/index.html YOU CAN SEE MY EXISTING BANNER IMAGE...IS THE SAME CONTENT I WANT ON THE CUSTOM BANNER IMAGE BUT I WANT THE BANNER IMAGE TO USE IMAGES TO PORTRAY WHAT THE CONTENT SAYS. POSSIBLE INTEGRATE AN INFOGRAPHIC DESIGN IN THE BANNER IMAGE. IM OPEN TO ALL IDEAS.

WHEN SOMEONE GOES TO MY WEBSITE, IMMEDIATELY I WANT THEM TO UNDERSTAND WHAT IT IS I DO.

MY BUSINESS PROVIDES OTHER BUSINESSES WITH THE ABILITY TO CREATE PROMOTIONAL GIVEAWAYS AND MARKETING PROMOTIONS USING GIFT VOUCHERS THAT ARE REDEEMABLE FOR FREE VACATIONS, CRUISES, ALL INCLUSIVE RESORT STAYS, TABLETS, SMARTWATCHES, DINING AND RESTAURANT INCENTIVES AND REWARDS AND MORE.

CURRENTLY THE CONTENT ON THE BANNER IMAGE IS THIS:
BOOST SALES & LEADS OVERNIGHT
BY ENTICING YOUR CUSTOMERS WITH FREE VACATION CERTIFICATES & OTHER HIGH PERCEIVED VALUE INCENTIVES

I HAVE ATTACHED A DOCUMENT WITH IMAGE ASSETTS YOU MAY REVIEW AND USE OR GET IDEAS FROM.

THE BOTTOM LINE IS MY SERVICE HELPS BUSINESSES INCREASE LEADS, CONVERSIONS, CTA, SALES, ETC WITHOUT HAVING TO INCREASE THEIR EXISTING AD SPEND. SIMPLY BY ADDING A FREE OFFER TO ALL THEIR EXISTING ADS WILL DRAMATICALLY INCREASE RESPONSE RATES. SO I WANT THIS BANNER TO REFLECT THIS SOMEHOW....MORE CUSTOMERS USING GIVEAWAYS!

Target Market(s)

B2B, SMALL BUSINESS OWNERS, ENTREPRENEURS, SOLOPRENEURS, MARKETING AGENCIES,

Industry/Entity Type

Digital Marketing

Requirements
Must have
• MUST PORTRAY THE RED CONTENT/TEXT USING IMAGES OF MY ASSETTS AND THE PORTRAY MORE CUSTOMERS---MUST BE FULLY CUSTOM

SIZE MUST BE: 1800x829
Nice to have
• USE CONTENT IN CURRENT BANNER IMAGE ALSO MAKE SURE TO USE THE FREE SAMPLE PKG BUTTON TOO.....MUST BE FULLY CUSTOM

SIZE MUST BE: 1800x829
Should not have
• MUST BE FULLY CUSTOM

SIZE MUST BE: 1800x829

```html
<!DOCTYPE html>
<html lang="en">
<head>
<meta charset="utf-8">
<title>Vantora Reward Incentives – Homepage Banner</title>
<link href="https://fonts.googleapis.com/css2?family=Arimo:wght@400;700&family=Montserrat:wght@800&family=Hind:wght@500;600&family=Oswald:wght@600&display=swap" rel="stylesheet">
<style>
  :root{
    --stage:#4a4a4a;
    --nav-blue:#1c6fc0;
    --nav-dark:#4b4f55;
    --signup-blue:#1f78c9;
    --phone-green:#39b54a;
    --cta-green:#17983a;
    --cta-green-dark:#0f7a2c;
    --tag-green:#178a3a;
    --ink:#111;
    --red:#e2242b;
    --white:#fff;
  }
  *{box-sizing:border-box;margin:0;padding:0}
  html,body{width:1200px;height:1200px;overflow:hidden;background:var(--stage)}
  body{position:relative;font-family:"Arimo",Arial,sans-serif}

  .site{position:absolute;left:160px;width:928px;height:486px;overflow:hidden;background:var(--white)}
  .site--photo{top:98px}
  .site--network{top:677px}

  /* header */
  .header{position:absolute;top:0;left:0;width:928px;height:62px;background:var(--nav-blue)}
  .header__brand{position:absolute;left:0;top:0;width:212px;height:62px;background:var(--white);
    clip-path:polygon(0 0,100% 0,196px 100%,0 100%)}
  .brand{position:absolute;left:14px;top:22px;display:flex;align-items:center;gap:6px;
    font:700 13px/1 "Arimo",Arial,sans-serif;color:var(--nav-blue);letter-spacing:.3px}
  .brand__mark{width:14px;height:14px;background:var(--nav-blue)}
  .nav{position:absolute;left:232px;top:0;height:62px;display:flex;align-items:center}
  .nav a{color:var(--white);text-decoration:none;font-size:10px;padding:0 10px;border-right:1px solid rgba(255,255,255,.25)}
  .nav a:last-child{border-right:0}
  .nav a.is-active{font-weight:700}
  .header__login,.header__signup{position:absolute;top:0;height:62px;width:46px;display:flex;flex-direction:column;
    align-items:center;justify-content:center;gap:4px;color:var(--white);font-size:8px}
  .header__login{left:707px;background:var(--nav-dark)}
  .header__signup{left:754px;background:var(--signup-blue)}
  .header__phone{position:absolute;left:801px;top:0;height:62px;width:127px;background:var(--phone-green);
    display:flex;align-items:center;gap:8px;padding-left:10px;color:var(--white)}
  .header__phone span{font-size:10px;line-height:1.5}
  .header__phone b{font-size:11px}

  /* hero */
  .hero{position:absolute;top:62px;left:0;width:928px;height:424px;overflow:hidden}
  .hero__backdrop{position:absolute;inset:0}
  .site--photo .hero__backdrop{background:
      radial-gradient(ellipse at 62% 60%,rgba(180,120,70,.55),transparent 40%),
      linear-gradient(180deg,#1d7fd4 0%,#6db6ea 35%,#e8f6fb 58%,#7fd3d8 78%,#cdeff0 100%)}
  .site--network .hero__backdrop{background:radial-gradient(ellipse at 35% 40%,#eeeff1 0%,#d9dbdf 55%,#c4c7cc 100%)}
  .hero__tiles{position:absolute;inset:0}
  .hero__copy{position:absolute;left:0;top:0}
  .headline{position:absolute;white-space:nowrap;text-transform:uppercase}
  .site--photo .headline{left:40px;top:66px;font:800 37px/38px "Montserrat",sans-serif;color:var(--white);letter-spacing:.5px}
  .site--network .headline{left:40px;top:62px;font:600 40px/41px "Hind",sans-serif;color:var(--red)}
  .subline{position:absolute;white-space:nowrap;font-family:"Arimo",Arial,sans-serif;color:var(--ink);text-transform:uppercase}
  .site--photo .subline{left:47px;top:150px;font-size:17px;line-height:24px}
  .site--network .subline{left:42px;top:150px;font-size:19.5px;line-height:27px}
  .tagline{position:absolute;white-space:nowrap;font-family:"Arimo",Arial,sans-serif;color:var(--tag-green);font-size:21px}
  .site--photo .tagline{left:47px;top:234px}
  .site--network .tagline{left:48px;top:248px}
  .cta{position:absolute;left:143px;top:310px;width:230px;height:54px;background:var(--cta-green);
    clip-path:polygon(0 0,100% 0,98% 88%,50% 100%,2% 88%);text-align:center;color:var(--white);
    box-shadow:inset 0 -4px 0 var(--cta-green-dark);padding-top:8px}
  .cta__label{display:block;font:600 19px/1 "Oswald",sans-serif}
  .cta__note{display:block;font-size:10.5px;margin-top:5px;letter-spacing:.3px}
</style>
</head>
<body>

<section class="site site--photo">
  <header class="header">
    <div class="header__brand"><div class="brand"><i class="brand__mark"></i>VANTORA REWARDS</div></div>
    <nav class="nav"><a>Home</a><a class="is-active">Our Incentives</a><a>Samples</a><a>Affiliates</a><a>Testimonials</a><a>Faq</a><a>Contact Us</a></nav>
    <div class="header__login"><svg width="12" height="13" viewBox="0 0 12 13"><circle cx="6" cy="3.5" r="3" fill="#fff"/><path d="M0 13c0-4 3-6 6-6s6 2 6 6z" fill="#fff"/></svg>LOGIN</div>
    <div class="header__signup"><svg width="14" height="14" viewBox="0 0 14 14"><circle cx="7" cy="7" r="6" fill="none" stroke="#fff" stroke-width="1.3"/><path d="M7 10.5V4M4.5 6.5 7 4l2.5 2.5" fill="none" stroke="#fff" stroke-width="1.4"/></svg>SIGN UP</div>
    <div class="header__phone"><svg width="14" height="26" viewBox="0 0 14 26"><rect x="1" y="1" width="12" height="24" rx="2" fill="none" stroke="#fff" stroke-width="2"/><rect x="3" y="4" width="8" height="15" fill="#fff"/></svg><span>USA Office :<br><b>555-204-7731</b></span></div>
  </header>
  <div class="hero">
    <div class="hero__backdrop" role="img" aria-label="Soft-focus tropical beach with longtail boat and turquoise water"></div>
    <svg class="hero__tiles" width="928" height="424" viewBox="0 0 928 424">
      <defs>
        <linearGradient id="seaA" x1="0" y1="0" x2="0" y2="1"><stop offset="0" stop-color="#2d4f7a"/><stop offset=".6" stop-color="#dfe4ea"/><stop offset="1" stop-color="#1f3e66"/></linearGradient>
        <linearGradient id="fuelA" x1="0" y1="0" x2="1" y2="1"><stop offset="0" stop-color="#e8ecee"/><stop offset=".5" stop-color="#2f9a4e"/><stop offset="1" stop-color="#3a3d40"/></linearGradient>
        <linearGradient id="mealA" x1="0" y1="0" x2="0" y2="1"><stop offset="0" stop-color="#f1ebe3"/><stop offset=".6" stop-color="#e7b25a"/><stop offset="1" stop-color="#7fae4a"/></linearGradient>
        <linearGradient id="roomA" x1="0" y1="0" x2="1" y2="1"><stop offset="0" stop-color="#8b6a48"/><stop offset=".5" stop-color="#e9dfd0"/><stop offset="1" stop-color="#b3262f"/></linearGradient>
        <linearGradient id="beachA" x1="0" y1="0" x2="0" y2="1"><stop offset="0" stop-color="#5a7f6a"/><stop offset="1" stop-color="#a36a3d"/></linearGradient>
      </defs>
      <g stroke="#fff" stroke-width="4">
        <polygon role="img" aria-label="Longtail boats at a tropical island" points="667,-116 785,2 667,120 549,2" fill="url(#beachA)"/>
        <polygon role="img" aria-label="Cruise ship at sea" points="800,-23 918,95 800,213 682,95" fill="url(#seaA)"/>
        <polygon role="img" aria-label="Hand holding a green fuel nozzle at a car" points="663,89 781,207 663,325 545,207" fill="url(#fuelA)"/>
        <polygon role="img" aria-label="Family sharing a meal at a dining table" points="800,219 918,337 800,455 682,337" fill="url(#mealA)"/>
        <polygon role="img" aria-label="Resort hotel bedroom" points="936,96 1054,214 936,332 818,214" fill="url(#roomA)"/>
        <polygon role="img" aria-label="Hotel room interior" points="667,300 785,418 667,536 549,418" fill="url(#roomA)"/>
        <polygon role="img" aria-label="Island coastline" points="936,-140 1054,-22 936,96 818,-22" fill="url(#beachA)"/>
        <polygon role="img" aria-label="Hotel room interior" points="936,332 1054,450 936,568 818,450" fill="url(#roomA)"/>
      </g>
    </svg>
    <h1 class="headline">Boost Sales &amp; Leads<br>Overnight</h1>
    <p class="subline">By enticing your customers with free<br>vacation certificates &amp; other high<br>perceived value incentives</p>
    <p class="tagline">Get Free Samples Now For A Limited Time !</p>
    <a class="cta"><span class="cta__label">GET FREE SAMPLES</span><span class="cta__note">100% FREE</span></a>
  </div>
</section>

<section class="site site--network">
  <header class="header">
    <div class="header__brand"><div class="brand"><i class="brand__mark"></i>VANTORA REWARDS</div></div>
    <nav class="nav"><a>Home</a><a class="is-active">Our Incentives</a><a>Samples</a><a>Affiliates</a><a>Testimonials</a><a>Faq</a><a>Contact Us</a></nav>
    <div class="header__login"><svg width="12" height="13" viewBox="0 0 12 13"><circle cx="6" cy="3.5" r="3" fill="#fff"/><path d="M0 13c0-4 3-6 6-6s6 2 6 6z" fill="#fff"/></svg>LOGIN</div>
    <div class="header__signup"><svg width="14" height="14" viewBox="0 0 14 14"><circle cx="7" cy="7" r="6" fill="none" stroke="#fff" stroke-width="1.3"/><path d="M7 10.5V4M4.5 6.5 7 4l2.5 2.5" fill="none" stroke="#fff" stroke-width="1.4"/></svg>SIGN UP</div>
    <div class="header__phone"><svg width="14" height="26" viewBox="0 0 14 26"><rect x="1" y="1" width="12" height="24" rx="2" fill="none" stroke="#fff" stroke-width="2"/><rect x="3" y="4" width="8" height="15" fill="#fff"/></svg><span>USA Office :<br><b>555-204-7731</b></span></div>
  </header>
  <div class="hero">
    <div class="hero__backdrop" role="img" aria-label="Light grey background with a faint connected network pattern"></div>
    <svg class="hero__tiles" width="928" height="424" viewBox="0 0 928 424">
      <defs>
        <linearGradient id="seaB" x1="0" y1="0" x2="0" y2="1"><stop offset="0" stop-color="#2d4f7a"/><stop offset=".6" stop-color="#dfe4ea"/><stop offset="1" stop-color="#1f3e66"/></linearGradient>
        <linearGradient id="fuelB" x1="0" y1="0" x2="1" y2="1"><stop offset="0" stop-color="#e8ecee"/><stop offset=".5" stop-color="#2f9a4e"/><stop offset="1" stop-color="#3a3d40"/></linearGradient>
        <linearGradient id="mealB" x1="0" y1="0" x2="0" y2="1"><stop offset="0" stop-color="#f1ebe3"/><stop offset=".6" stop-color="#e7b25a"/><stop offset="1" stop-color="#7fae4a"/></linearGradient>
        <linearGradient id="roomB" x1="0" y1="0" x2="1" y2="1"><stop offset="0" stop-color="#8b6a48"/><stop offset=".5" stop-color="#e9dfd0"/><stop offset="1" stop-color="#b3262f"/></linearGradient>
      </defs>
      <g stroke="#fff" stroke-width="4">
        <polygon role="img" aria-label="Cruise ship at sea" points="753,-55 874,66 753,187 632,66" fill="url(#seaB)"/>
        <polygon role="img" aria-label="Hand holding a green fuel nozzle at a car" points="620,79 741,200 620,321 499,200" fill="url(#fuelB)"/>
        <polygon role="img" aria-label="Resort hotel bedroom" points="887,79 1008,200 887,321 766,200" fill="url(#roomB)"/>
        <polygon role="img" aria-label="Family sharing a meal at a dining table" points="753,209 874,330 753,451 632,330" fill="url(#mealB)"/>
      </g>
    </svg>
    <h1 class="headline">Boost Sales &amp; Leads<br>Overnight</h1>
    <p class="subline">By enticing your customers with free<br>vacation certificates &amp; other high<br>perceived value incentives</p>
    <p class="tagline">Get Free Samples Now For A Limited Time !</p>
    <a class="cta"><span class="cta__label">GET FREE SAMPLES</span><span class="cta__note">100% FREE</span></a>
  </div>
</section>

</body>
</html>
```